Communication of Recommended Belief Letter

To Whom This May Concern,

My company's name is Brookfane LLC. I would like to send electronic messages to my clients. Therefore, I would like PixelForge to create a letterhead template to say Brookfane- without the LLC. My messages could extend up to 20 pages long. I would like something that is chic, fancy, and has creative designs. The background color should be white. The creative designs are open for suggestions without color restrictions. Font type and color are also open for suggestions. It may be what you believe best suite's the letterhead. I would like the letterhead to include the company logo. Please see attachment for file. Thank you.

Target Market(s)

working class American's

Industry/Entity Type

Communication

Contact Information for Business Card

The business card should be chic and fancy.

Font styles to use
Script

Requirements
Must have
• Company name: Brookfane LLC
• Company symbol: Please see attachment
• Name: Moriel Haskins
• Title: President
• Company website: www.brookfanellc-example.com
Nice to have
• Open for suggestions

```html
<!DOCTYPE html>
<html lang="en">
<head>
<meta charset="utf-8">
<title>Brookfane LLC Letterhead</title>
<link rel="stylesheet" href="https://fonts.googleapis.com/css2?family=Cinzel:wght@400;600&family=Arimo:wght@400;700&display=swap">
<style>
  :root {
    --backdrop: #b9b9b9;
    --paper: #ffffff;
    --gold: #b8862a;
    --band: #e0920f;
    --ink: #3a3a3a;
    --ink-strong: #1e1e1e;
  }
  * { box-sizing: border-box; margin: 0; padding: 0; }
  html, body { width: 1200px; height: 795px; overflow: hidden; }
  body {
    background: radial-gradient(ellipse at 45% 35%, #d4d4d4 0%, var(--backdrop) 70%, #a6a6a6 100%);
    position: relative;
  }
  .letterhead {
    position: absolute;
    left: 331px; top: 18px;
    width: 538px; height: 760px;
    background: var(--paper);
    box-shadow: 0 6px 18px rgba(0,0,0,.25);
    font-family: "Arimo", Arial, sans-serif;
    color: var(--ink);
    overflow: hidden;
  }
  .brand {
    position: absolute; top: 46px; left: 0; right: 0;
    display: flex; align-items: center; justify-content: center; gap: 10px;
  }
  .brand-dot { width: 14px; height: 14px; border-radius: 50%; background: var(--gold); }
  .brand-name {
    font-family: "Cinzel", Georgia, serif;
    font-weight: 400; font-size: 21px; letter-spacing: 1.5px;
    color: var(--gold);
  }
  .letter-body {
    position: absolute; top: 150px; left: 52px; right: 52px;
    font-size: 9.6px; line-height: 1.32;
  }
  .salutation { font-weight: 700; font-size: 11px; color: var(--ink-strong); margin-bottom: 12px; }
  .letter-body p { margin-bottom: 12px; text-align: justify; }
  .signature {
    position: absolute; top: 425px; left: 54px;
    width: 110px; height: 42px;
    background: linear-gradient(90deg, #e4e4e4, #f3f3f3);
    border-radius: 4px;
  }
  .signatory {
    position: absolute; right: 52px; bottom: 62px; text-align: right;
  }
  .signatory-name {
    font-family: "Cinzel", Georgia, serif; font-weight: 600;
    font-size: 13px; color: var(--gold); letter-spacing: .5px;
  }
  .signatory-title {
    font-family: "Cinzel", Georgia, serif; font-size: 11px;
    color: var(--ink-strong); letter-spacing: 1px; margin-top: 2px;
  }
  .footer-band { position: absolute; left: 0; bottom: 0; width: 538px; height: 50px; }
  .website {
    position: absolute; right: 22px; bottom: 19px;
    font-family: "Cinzel", Georgia, serif; font-size: 9.5px;
    color: #fff; letter-spacing: .8px;
  }
</style>
</head>
<body>
  <main class="letterhead">
    <header class="brand">
      <span class="brand-dot"></span>
      <span class="brand-name">Brookfane LLC</span>
    </header>

    <section class="letter-body">
      <p class="salutation">Dear Mr. Calder,</p>
      <p>Lorem Ipsum is simply dummy text of the printing and typesetting industry. Lorem Ipsum has been the industry's standard dummy text ever since the 1500s, when an unknown printer took a galley of type and scrambled it to make a type specimen book. It has survived not only five centuries, but also the leap into electronic typesetting, remaining essentially unchanged.</p>
      <p>The standard chunk of Lorem Ipsum used since the 1500s is reproduced below for those interested. Sections 1.10.32 and 1.10.33 from "de Finibus Bonorum et Malorum" by Corvinus are also reproduced in their exact original form, accompanied by English versions from the 1914 translation by H. Redfern.</p>
      <p>Lorem Ipsum is simply dummy text of the printing and typesetting industry. Lorem Ipsum has been the industry's standard dummy text ever since the 1500s, when an unknown printer took a galley of type and scrambled it to make a type specimen book. It has survived not only five centuries, but also the leap into electronic typesetting, remaining essentially unchanged. It was popularised in the</p>
    </section>

    <div class="signature" role="img" aria-label="Handwritten signature of the sender"></div>

    <div class="signatory">
      <div class="signatory-name">Moriel Haskins</div>
      <div class="signatory-title">President</div>
    </div>

    <svg class="footer-band" viewBox="0 0 538 50" aria-hidden="true">
      <path d="M0 42 H300 Q312 42 318 33 L322 26 Q328 17 340 17 H538 V46 H0 Z" fill="var(--gold)"/>
      <rect x="0" y="42" width="538" height="4" fill="var(--band)"/>
    </svg>
    <div class="website">www.brookfanellc-example.com</div>
  </main>
</body>
</html>
```